Book Cover for Notes on the Quiet River's Far Lamps

I need a book cover for a 6 x 9 paperback titled Notes on the Quiet River's Far Lamps Gathered by Sailors and Weavers Resting in the Valley beyond the Northern Valley. It has to do with consciousness, the mind, incarnation onto Earth, leaving Earth, and the life in the life after this life. I have an idea I'm providing with this description, but I am open to anything that would be striking and stimulating, whether with a book or not. I am the author, T. Warren Blakely. I've added another background idea to see if anyone can do something with it and I've increased the budget.

```html
<!DOCTYPE html>
<html lang="en">
<head>
<meta charset="utf-8">
<title>Notes on the Quiet River's Far Lamps — Cover Wrap</title>
<link rel="stylesheet" href="https://fonts.googleapis.com/css2?family=Cinzel:wght@400;600&family=Della+Respira&family=EB+Garamond:wght@500&display=swap">
<style>
  :root {
    --leather-dark: #2a1208;
    --leather-mid: #5a2a16;
    --leather-light: #8a5430;
    --tooling: #3b1a0c;
    --tooling-edge: #6e3a1e;
    --panel-center: #7f4a28;
    --panel-edge: #4a2312;
    --gold: #e8c870;
    --gold-deep: #b88c3a;
    --cream: #f2e6cc;
    --spine: #2c130a;
  }
  * { margin: 0; padding: 0; box-sizing: border-box; }
  html, body { width: 1200px; height: 875px; overflow: hidden; background: var(--leather-dark); }
  .wrap {
    position: relative; width: 1200px; height: 875px; overflow: hidden;
    background: radial-gradient(ellipse at 50% 50%, var(--leather-mid) 0%, var(--leather-dark) 100%);
  }
  .board {
    position: absolute; top: 0; height: 875px;
    background: linear-gradient(180deg, #4e2312 0%, #6a3419 50%, #4a2111 100%);
  }
  .board--back { left: 0; width: 565px; }
  .board--front { left: 629px; width: 571px; }
  .tooled-border {
    position: absolute;
    background: linear-gradient(135deg, var(--tooling) 0%, var(--tooling-edge) 50%, var(--tooling) 100%);
    border: 3px solid #24100a;
    box-shadow: inset 0 0 0 6px rgba(0,0,0,.25), 0 0 12px rgba(0,0,0,.6);
  }
  .board--back .tooled-border { left: 28px; top: 36px; width: 506px; height: 800px; }
  .board--front .tooled-border { left: 34px; top: 36px; width: 506px; height: 800px; }
  .panel {
    position: absolute;
    background: radial-gradient(ellipse at 50% 45%, var(--panel-center) 0%, #65361c 55%, var(--panel-edge) 100%);
    border: 2px solid #1f0d06;
    box-shadow: 0 0 0 6px #3a1a0c, 0 0 0 8px #22100a, inset 0 0 30px rgba(0,0,0,.55);
  }
  .panel--back { left: 112px; top: 128px; width: 380px; height: 623px; }
  .panel--front { left: 74px; top: 128px; width: 421px; height: 618px; }

  .spine {
    position: absolute; left: 565px; top: 0; width: 64px; height: 875px;
    background: linear-gradient(90deg, #1c0b05 0%, var(--spine) 30%, #3a1a0c 50%, var(--spine) 70%, #1c0b05 100%);
    border-left: 2px solid #5b3016; border-right: 2px solid #5b3016;
  }
  .spine-dot {
    position: absolute; left: 50%; width: 14px; height: 14px; margin-left: -7px;
    border: 1.5px solid var(--gold-deep); border-radius: 50%;
  }
  .spine-dot--top { top: 16px; }
  .spine-dot--bottom { bottom: 16px; }
  .spine-title, .spine-author {
    position: absolute; left: 50%; transform: translateX(-50%);
    writing-mode: vertical-rl; color: var(--gold); white-space: nowrap;
  }
  .spine-title {
    top: 100px; font-family: "Cinzel", serif; font-size: 16px; letter-spacing: .5px;
  }
  .spine-author {
    top: 565px; font-family: "Della Respira", serif; font-size: 22px;
  }

  .back-title {
    position: absolute; left: 112px; top: 166px; width: 380px;
    text-align: center; font-family: "Cinzel", serif; font-weight: 600;
    font-size: 19px; line-height: 25px; color: var(--cream);
    text-shadow: 0 1px 3px rgba(0,0,0,.6);
  }
  .back-blurb {
    position: absolute; left: 130px; top: 358px; width: 345px;
    text-align: center; font-family: "EB Garamond", serif; font-weight: 500;
    font-size: 13px; line-height: 16.5px; color: #fff8ea;
  }
  .fleuron {
    position: absolute; width: 34px; height: 22px; border-radius: 40% 40% 50% 50%;
    background: radial-gradient(ellipse, var(--gold) 0%, var(--gold-deep) 70%, transparent 72%);
  }
  .fleuron--back { left: 285px; top: 287px; }
  .fleuron--front { left: 889px; top: 650px; }

  .front-title {
    position: absolute; left: 703px; top: 205px; width: 421px; text-align: center;
    font-family: "Della Respira", serif; color: var(--cream);
    text-shadow: 0 2px 4px rgba(0,0,0,.6);
  }
  .front-title .lead {
    display: block; font-size: 72px; line-height: 80px; color: var(--gold);
    text-shadow: 0 2px 0 #7a5518, 0 4px 8px rgba(0,0,0,.7);
  }
  .front-title .rest { display: block; font-size: 36px; line-height: 48px; }
  .divider { position: absolute; top: 452px; left: 0; }
  .subtitle {
    position: absolute; left: 733px; top: 476px; width: 361px; text-align: center;
    font-family: "Della Respira", serif; font-size: 25px; line-height: 36px;
    color: var(--cream); text-shadow: 0 1px 3px rgba(0,0,0,.6);
  }
  .author {
    position: absolute; left: 703px; top: 690px; width: 421px; text-align: center;
    font-family: "Della Respira", serif; font-size: 34px; color: var(--gold);
    text-shadow: 0 2px 4px rgba(0,0,0,.7);
  }
</style>
</head>
<body>
<main class="wrap">
  <section class="board board--back">
    <div class="tooled-border" role="img" aria-label="Tooled leather border with carved scrollwork and brass corner studs"></div>
    <div class="panel panel--back"></div>
  </section>

  <section class="spine">
    <span class="spine-dot spine-dot--top"></span>
    <span class="spine-title">NOTES ON THE QUIET RIVER'S FAR LAMPS</span>
    <span class="spine-author">T. Warren Blakely</span>
    <span class="spine-dot spine-dot--bottom"></span>
  </section>

  <section class="board board--front">
    <div class="tooled-border" role="img" aria-label="Tooled leather border with carved scrollwork and brass corner studs"></div>
    <div class="panel panel--front"></div>
  </section>

  <h2 class="back-title">Notes on the Quiet River's Far Lamps Gathered by Sailors and Weavers Resting in the Valley beyond the Northern Valley</h2>
  <div class="fleuron fleuron--back" role="img" aria-label="Gold fleur ornament"></div>
  <p class="back-blurb">Lorem ipsum dolor sit amet, consectetur adipisicing elit, sed do eiusmod tempor incididunt ut labore et dolore magna aliqua. Ut enim ad minim veniam, quis nostrud exercitation ullamco laboris nisi ut aliquip ex ea commodo consequat. Duis aute irure dolor in reprehenderit in voluptate velit esse cillum dolore eu fugiat nulla pariatur. Excepteur sint occaecat cupidatat non proident, sunt in culpa qui officia deserunt mollit anim id est laborum. Sed ut perspiciatis unde omnis iste natus error sit voluptatem accusantium.</p>

  <h1 class="front-title">
    <span class="lead">Notes</span>
    <span class="rest">on the Quiet River's</span>
    <span class="rest">Far Lamps</span>
  </h1>
  <svg class="divider" width="1200" height="10" viewBox="0 0 1200 10" aria-hidden="true">
    <line x1="812" y1="5" x2="900" y2="5" stroke="#e8c870" stroke-width="1.5"/>
    <line x1="928" y1="5" x2="1016" y2="5" stroke="#e8c870" stroke-width="1.5"/>
    <circle cx="812" cy="5" r="3" fill="#e8c870"/>
    <circle cx="1016" cy="5" r="3" fill="#e8c870"/>
  </svg>
  <p class="subtitle">Gathered by Sailors and Weavers Resting in the Valley beyond the Northern Valley</p>
  <div class="fleuron fleuron--front" role="img" aria-label="Gold fleur ornament"></div>
  <p class="author">T. Warren Blakely</p>
</main>
</body>
</html>
```